Rack Card Design Project

We are a locally family owned public golf course. We would like to have a rack card designed that can be used for multiple applications. The colors in our logo are grey, blue, and white. Please use those in the card design. The company logo, contact information, address, and summer pricing should be included. I've included some pictures that may or may not be used. I'm also open to suggestions....use one photo, multiple photos, a stock photo or image representing golf etc.

```html
<!DOCTYPE html>
<html lang="en">
<head>
<meta charset="utf-8">
<title>The Banks of Heron Creek – Rack Card</title>
<link rel="stylesheet" href="https://fonts.googleapis.com/css2?family=Libre+Caslon+Text:ital,wght@0,400;0,700;1,400&display=swap">
<style>
:root{
  --navy:#0d3058;
  --grey:#8c8c8c;
  --grey-mid:#8a8a8a;
  --grey-light:#d4d4d4;
  --white:#ffffff;
}
*{margin:0;padding:0;box-sizing:border-box}
html,body{width:1199px;height:1200px;overflow:hidden;background:var(--white)}
body{position:relative;font-family:"Libre Caslon Text",Georgia,serif;color:var(--navy)}
.card{position:absolute;top:20px;width:526px;height:1146px;overflow:hidden;background:var(--white)}
.card--front{left:74px}
.card--back{left:637px}
.band{position:absolute;left:0;width:100%}
.navy{background:var(--navy)}
.grey{background:var(--grey)}
.line{position:absolute;left:0;right:0;text-align:center;white-space:nowrap}
.caps{font-weight:700;text-transform:uppercase}
.italic{font-style:italic}

/* front */
.photo{position:absolute;left:0;top:206px;width:100%;height:708px;
  background:linear-gradient(180deg,#b9c9d8 0%,#dfe0da 30%,#e9d9bb 44%,#55623c 56%,#3f5029 70%,#4b5c33 85%,#3a4927 100%)}
.badge{position:absolute;left:126px;top:81px;width:264px;height:264px;border-radius:50%;
  background:var(--grey);display:flex;align-items:center;justify-content:center;text-align:center}
.badge__name{color:var(--white);font-weight:700;font-size:22px;line-height:1.3;text-transform:uppercase}
.front-title{color:var(--white);font-size:39px;line-height:48px}
.front-place{color:var(--white);font-size:28px}
.front-cta{color:var(--white);font-size:29px}
.front-contact{color:var(--white);font-size:27px;font-weight:700}

/* back */
.back-title{color:var(--white);font-size:35px;line-height:43px}
.rates-title{font-size:29px;font-weight:700}
.rates-dates{font-size:27px}
.rate-table{position:absolute;left:95px;top:265px;width:322px;border-collapse:collapse;font-size:21px;font-weight:700}
.rate-table th{background:#808080;color:var(--white);height:38px;font-size:21px;text-transform:uppercase}
.rate-table td{height:40px;background:var(--grey-light)}
.rate-table tr.alt td{background:var(--grey-mid);height:36px}
.rate-table td.time{padding-left:50px;text-align:left}
.rate-table td.price{text-align:left;padding-left:12px}
.nine{font-size:22px}
.walk{font-size:19px;font-weight:700}
.kids{font-size:16px;font-weight:700}
.lunch{font-size:18px;font-weight:700;line-height:19px}
.divider{position:absolute;left:61px;top:689px;width:406px;height:5px;background:var(--navy)}
.divider-dot{position:absolute;left:214px;top:648px;width:88px;height:88px;border-radius:50%;background:var(--grey)}
.connect{font-size:21px}
.club{font-size:19px;font-weight:700;text-transform:uppercase}
.addr{font-size:21px}
.phone{font-size:27px;font-weight:700}
.web{font-size:21px;font-weight:700}
.social{font-size:16px;display:flex;justify-content:center;align-items:center;gap:8px}
.social__mark{width:26px;height:26px;background:var(--navy);display:inline-block}
.directions{color:var(--white);font-size:16px;line-height:22px}
</style>
</head>
<body>

<section class="card card--front">
  <div class="band navy" style="top:0;height:186px"></div>
  <div class="band grey" style="top:186px;height:20px"></div>
  <div class="photo" role="img" aria-label="Golf course fairway at sunrise with pine trees and soft clouds"></div>
  <div class="band grey" style="top:914px;height:20px"></div>
  <div class="band navy" style="top:934px;height:212px"></div>

  <div class="badge"><span class="badge__name">The Banks<br>of Heron Creek<br>Golf Club</span></div>

  <div class="line caps front-title" style="top:712px">The Banks<br>of Heron Creek</div>
  <div class="line italic front-place" style="top:838px">Palm Haven, Florida</div>

  <div class="line caps front-cta" style="top:964px">Book Tee Times Online</div>
  <div class="line front-contact" style="top:1006px">www.heroncreekgc.com</div>
  <div class="line front-contact" style="top:1048px;font-weight:400">555.014.2837</div>
</section>

<section class="card card--back">
  <div class="band navy" style="top:0;height:126px"></div>
  <div class="band grey" style="top:126px;height:18px"></div>
  <div class="band grey" style="top:1000px;height:20px"></div>
  <div class="band navy" style="top:1020px;height:126px"></div>

  <div class="line caps back-title" style="top:28px">The Banks<br>of Heron Creek</div>

  <div class="line rates-title" style="top:175px">Summer Rates</div>
  <div class="line italic rates-dates" style="top:210px">May 1 – September 30</div>

  <table class="rate-table">
    <tr><th colspan="2">18 Holes with Cart</th></tr>
    <tr><td class="time">7AM – 11AM</td><td class="price">$24</td></tr>
    <tr class="alt"><td class="time">11AM – 3PM</td><td class="price">$19</td></tr>
    <tr><td class="time">3PM – Close</td><td class="price">$15</td></tr>
  </table>

  <div class="line caps nine" style="top:463px">9 Holes with Cart - $15</div>
  <div class="line walk" style="top:505px">Walking - $12</div>
  <div class="line kids" style="top:545px">*Children 15 and Under FREE with Paid Adult</div>
  <div class="line lunch" style="top:585px">Lunch Available Daily<br>10AM – 3PM</div>

  <div class="divider"></div>
  <div class="divider-dot"></div>

  <div class="line italic connect" style="top:740px">Connect with us</div>
  <div class="line club" style="top:784px">The Banks of Heron Creek Golf Club</div>
  <div class="line addr" style="top:811px">2450 NW Willow Bend Road</div>
  <div class="line addr" style="top:840px">Palm Haven, FL 34000</div>
  <div class="line phone" style="top:887px">555.014.2837</div>
  <div class="line web" style="top:918px">www.heroncreekgc.com</div>
  <div class="line italic social" style="top:958px"><span class="social__mark"></span><span>HeronCreekGolf/</span></div>

  <div class="line italic directions" style="top:1039px">Located North Of The Cypress Bridge in<br>The Heron Creek Subdivision, West Of Rt. 9<br>And 1 Block Off The East Fork Of The Willow River.</div>
</section>

</body>
</html>
```